Corporate Web Design

Hello Designers,
Thank you for wanting to participate in designing a web design.
First off let me introduce ourselves, we are a precious metals refinery that is base in the west coast. Our Name is Sterling Harbor Metals Refinery. Our sole goal for this website is simplicity yet cleanliness and elegance. We want to demonstrate the process and procedures of what we do and who we are.
The Lay out:
We want about 4-5 Tabs that will help guide our customers through our website with ease. Some ideas of what we want to call the tabs might be….
1. Home
- This tab will take them to the home page
2. Contact Us
- Our contact information
- Client contact form
- Some sort of membership form?
3. Pick-up Service
- This tab will explain how this process works and what it in tells.
- This page will also have a section for requirements.
- This pickup service will only be available for members and people that have a good account with us.
4. How it Works
- This page will explain who we are and how we work.
- I would like to somehow creatively show the process and the steps we take in melting their gold.
Effects:
An effect that I would want to see is a live precious metal stock price. This price will automatically update and post the most recent and current price on the market of what the gold, silver etc prices. Here is a link of a company that has something similar, http://qlvt-refining.example/ what I like about this spot price pop up, is that it follows them all over the page. I like that idea.
I would also like some sort of slide show that has videos and demonstrations of our company and business.
These are all Websites of our competitors that we like many ideas from.
http://www.bzkw.example/
What we like about this website is the tab that says “Request Pick-up” With a form that they have to fill out. We would want more than just a form; we would want some sort of membership application.
http://vexmetals.example/
What I like about this website is the slideshow. It’s very simple yet professional. This is something that I would like to incorporate into our website. I also like the live metal market price.
http://qlvt-refining.example/
This is another example of a website that has a live spot price of the gold market. I like how the gold price follows you around the page. I would like to see some of your ideas with this.
http://www.dunmetals.example/
This website is very clean and simple. I like the colors. I would like a little more character than what they have but I like the simplicity.
The colors we like are black, white, silver, gold, Royal Blue etc; basically anything that creates a clean atmosphere. These colors match our logo and also have a very elegant and professional perception to them. Please do not limit yourselves to only our suggestions
These are links to our Logo with all different colors.
https://files.example/s/k27m4p91rtz8vqa/LOGO_black_background.png
https://files.example/s/9wnb3x61hdq2lfe/LOGO_black.png
https://files.example/s/m8rc215jqpv4kzo/LOGO_transparent_background.png
https://files.example/s/t3fy804lwmn6bsu/LOGO_white_background.png
These are links to a brochure of our business that represents and shows the process of what we do and demonstrates who we are.
https://files.example/s/h6dv592kqcx1rwa/inside_1.pdf
https://files.example/s/p4gl736nybe9tcu/inside_2.pdf
Bottom line we want to see examples of ideas and layouts that you have for a website. Please upload them and We will comment back on them.

```html
<!DOCTYPE html>
<html lang="en">
<head>
<meta charset="utf-8">
<title>Sterling Harbor Metals Refinery</title>
<link rel="stylesheet" href="https://fonts.googleapis.com/css2?family=PT+Sans:ital,wght@0,400;0,700;1,400&family=PT+Sans+Narrow:wght@400;700&display=swap">
<style>
:root{
  --black:#000;
  --gold:#b99a56;
  --gold-light:#d7bd86;
  --gold-dark:#7a6236;
  --text-muted:#7d7d7d;
  --white:#fff;
  --nav-top:#6d6d6d;
  --nav-bottom:#3f3f3f;
  --red:#c4120f;
  --footer:#2a2a2a;
}
*{margin:0;padding:0;box-sizing:border-box}
html,body{width:1171px;height:1200px;overflow:hidden;background:var(--black)}
body{position:relative;font-family:"PT Sans",sans-serif;color:var(--white)}
.abs{position:absolute}

/* header */
.brand{left:199px;top:34px;font-family:"PT Sans",sans-serif;font-size:26px;letter-spacing:2px;color:var(--gold-light);text-transform:uppercase;font-weight:400;white-space:nowrap}
.lang{left:708px;top:43px;width:85px;height:21px;background:linear-gradient(#fff,#d9d9d9);border-radius:3px;color:#555;font-size:10px;display:flex;align-items:center;padding-left:8px;gap:6px}
.lang .flag{width:14px;height:9px;background:#2a3f84;display:inline-block}
.lang svg{margin-left:auto;margin-right:6px}
.search{left:801px;top:43px;width:176px;height:21px;background:linear-gradient(#fff,#d9d9d9);border-radius:3px;color:#555;font-size:8px;display:flex;align-items:center;padding-left:14px}
.search svg{position:absolute;right:7px;top:4px}

/* navigation */
.nav{left:0;top:97px;width:1171px;height:59px;background:linear-gradient(var(--nav-top),var(--nav-bottom))}
.nav ul{list-style:none;position:absolute;left:176px;top:0;display:flex;height:59px;border-right:1px solid #2c2c2c}
.nav li{height:59px;border-left:1px solid #2c2c2c;padding:15px 0 0 20px}
.nav li.active{background:linear-gradient(#a2875a,#6a5535);border-left-color:#c0a46c}
.nav .title{display:block;font-family:"PT Sans Narrow",sans-serif;font-size:13px;text-transform:uppercase;color:var(--white)}
.nav .sub{display:block;font-size:10px;font-style:italic;color:#b5b5b5;margin-top:2px}
.nav li.active .sub{color:#e8d6ad}

/* slider */
.slider{left:176px;top:166px;width:819px;height:343px;background:radial-gradient(ellipse at 65% 45%,#d8b560 0%,#8c6c2c 35%,#3a3026 70%,#2a2624 100%)}
.slider-arrow{top:349px;width:24px;height:24px;border-radius:50%;background:rgba(40,40,40,.7)}
.slider-progress{left:176px;top:509px;width:285px;height:3px;background:var(--gold-dark)}

/* features */
.features{left:176px;top:509px;width:819px;height:97px;background:linear-gradient(90deg,#1b1916,#2b2721 50%,#1d1b18);display:flex}
.feature{flex:1;padding:35px 0 0 56px;border-left:1px solid var(--gold-dark)}
.feature:first-child{border-left:none}
.feature h3{font-family:"PT Sans Narrow",sans-serif;font-weight:400;font-size:20px;color:var(--gold);text-transform:uppercase;line-height:1}
.feature p{font-family:"PT Sans Narrow",sans-serif;font-size:10px;text-transform:uppercase;margin-top:6px}

/* welcome */
.welcome-title{left:189px;top:628px;font-family:"PT Sans Narrow",sans-serif;font-size:18px;color:var(--gold);text-transform:uppercase}
.welcome-photo{left:192px;top:670px;width:235px;height:164px;border:4px solid #3a3436;background:linear-gradient(120deg,#5e4a3c,#a5946f 50%,#d7d0c2)}
.intro{left:450px;top:673px;width:527px}
.intro h2{font-family:"PT Sans Narrow",sans-serif;font-weight:400;font-size:12px;text-transform:uppercase;margin-bottom:14px}
.intro p{font-size:8px;line-height:15px;color:var(--text-muted);margin-bottom:15px}

/* products */
.product{top:870px;width:251px;height:182px}
.product .art{height:132px}
.product .bar{height:50px;display:flex;align-items:center;justify-content:space-between;padding:0 8px 0 11px}
.product h4{font-family:"PT Sans Narrow",sans-serif;font-weight:400;font-size:22px;color:#6b5a3b;text-transform:uppercase}
.product .btn{font-family:"PT Sans Narrow",sans-serif;font-size:11px;text-transform:uppercase;color:var(--white);padding:7px 16px;border-radius:2px;background:linear-gradient(#dc2a22,#9e0c0a)}
.bar.gold{background:linear-gradient(#dccaa6,#9c8359)}
.bar.silver{background:linear-gradient(#f7f7f7,#c7c7c7)}
.bar.silver h4{color:#3c3c3c}
.bar.silver .btn{background:linear-gradient(#5b5b5b,#2b2b2b)}
.art.gold{background:radial-gradient(circle at 50% 50%,#e8c55c,#a57a1f 55%,#2a1e0c)}
.art.silver{background:radial-gradient(circle at 50% 50%,#f2f2f2,#9a9a9a 55%,#2b2b2b)}

/* footer */
.footer{left:0;top:1074px;width:1171px;height:53px;background:var(--footer)}
.footer-brand{left:199px;top:1092px;font-size:12px;letter-spacing:1px;color:var(--gold-light);text-transform:uppercase;white-space:nowrap}
.copyright{left:345px;top:1094px;font-size:9px;color:#b8b8b8;white-space:nowrap}
.social{top:1094px;width:12px;height:12px;border-radius:50%;background:#6a6a6a}

/* price bar */
.pricebar{left:0;top:1127px;width:1171px;height:73px;background:linear-gradient(#c9ae82,#9a7d52)}
.price-label{top:1142px;font-family:"PT Sans Narrow",sans-serif;font-size:9px;color:#2d2415;text-transform:uppercase}
.price-field{top:1163px;height:18px;border-radius:3px;background:linear-gradient(#8b7150,#6d583c);box-shadow:inset 0 1px 2px rgba(0,0,0,.4);font-size:7px;color:#efe4cc;display:flex;align-items:center;padding-left:8px;text-transform:uppercase}
.divider{top:1138px;width:1px;height:50px;background:#8a6f48;box-shadow:1px 0 0 #d8c49f}
</style>
</head>
<body>

<header>
  <div class="abs brand">Sterling Harbor</div>
  <div class="abs lang"><span class="flag"></span>English
    <svg width="7" height="5" viewBox="0 0 7 5"><path d="M0 0l3.5 4L7 0" fill="none" stroke="#555" stroke-width="1.4"/></svg>
  </div>
  <div class="abs search">SEARCH
    <svg width="12" height="12" viewBox="0 0 12 12"><circle cx="5" cy="5" r="3.8" fill="none" stroke="#888" stroke-width="1.5"/><path d="M8 8l3 3" stroke="#888" stroke-width="1.8"/></svg>
  </div>
</header>

<nav class="abs nav">
  <ul>
    <li class="active" style="width:156px"><span class="title">Home</span><span class="sub">Welcome to our Site</span></li>
    <li style="width:166px"><span class="title">Pickup Service</span><span class="sub">Get our services Free</span></li>
    <li style="width:166px"><span class="title">How it works</span><span class="sub">Did you know our works</span></li>
    <li style="width:166px"><span class="title">Scrap Calculator</span><span class="sub">Gold Scrap Caclulator</span></li>
    <li style="width:166px"><span class="title">Contact Us</span><span class="sub">Get in Touch</span></li>
  </ul>
</nav>

<div class="abs slider" role="img" aria-label="Photo of hands sorting scrap gold jewellery on a workbench"></div>
<div class="abs slider-arrow" style="left:185px">
  <svg width="24" height="24" viewBox="0 0 24 24"><path d="M14 7l-5 5 5 5" fill="none" stroke="#999" stroke-width="1.5"/></svg>
</div>
<div class="abs slider-arrow" style="left:962px">
  <svg width="24" height="24" viewBox="0 0 24 24"><path d="M10 7l5 5-5 5" fill="none" stroke="#999" stroke-width="1.5"/></svg>
</div>
<div class="abs slider-progress"></div>

<section class="abs features">
  <div class="feature"><h3>Request Pick-up</h3><p>Available at competitive premiums</p></div>
  <div class="feature"><h3>Silver Bars</h3><p>Available at competitive premiums</p></div>
  <div class="feature" style="flex:.77"><h3>Bullion</h3><p>Encyclopedia</p></div>
</section>

<h1 class="abs welcome-title" style="font-weight:400">Welcome to Sterling Harbor</h1>
<div class="abs welcome-photo" role="img" aria-label="Photo of two men shaking hands in the refinery office"></div>
<section class="abs intro">
  <h2>Lorem Ipsum is simply dummy text of the printing and typesetting industry.</h2>
  <p>Lorem Ipsum is simply dummy text of the printing and typesetting industry. Lorem Ipsum has been the industry's standard dummy text ever since the 1500s, when an unknown printer took a galley of type and scrambled it to make a type specimen book. It has survived not only five centuries, but also the leap into electronic typesetting, remaining essentially unchanged. It was popularised in the 1960s with the release of Letraset sheets containing Lorem Ipsum passages, and more recently with desktop publishing.</p>
  <p>Lorem Ipsum is simply dummy text of the printing and typesetting industry. Lorem Ipsum has been the industry's standard dummy text ever since the 1500s, when an unknown printer took a galley of type and scrambled it to make a type specimen book. It has survived not only five centuries, but also the leap into electronic typesetting, remaining essentially unchanged. It was popularised in the 1960s with the release of Letraset sheets containing.</p>
</section>

<article class="abs product" style="left:192px">
  <div class="art gold" role="img" aria-label="Gold bars and gold bullion coins"></div>
  <div class="bar gold"><h4>Gold Bullion</h4><span class="btn">More Details</span></div>
</article>
<article class="abs product" style="left:460px">
  <div class="art silver" role="img" aria-label="Silver bars surrounded by bullion coins"></div>
  <div class="bar gold"><h4>US Gold</h4><span class="btn">More Details</span></div>
</article>
<article class="abs product" style="left:727px">
  <div class="art silver" role="img" aria-label="Silver bullion bar and silver coins"></div>
  <div class="bar silver"><h4>Silver Bullion</h4><span class="btn">More Details</span></div>
</article>

<footer>
  <div class="abs footer"></div>
  <div class="abs footer-brand">Sterling Harbor</div>
  <div class="abs copyright">Copyrights ©2013. Sterling Harbor. All rights reserved.</div>
  <span class="abs social" style="left:833px"></span>
  <span class="abs social" style="left:866px"></span>
  <span class="abs social" style="left:900px"></span>
  <span class="abs social" style="left:933px"></span>
  <span class="abs social" style="left:965px"></span>

  <div class="abs pricebar"></div>
  <span class="abs price-label" style="left:198px">Real-time price</span>
  <div class="abs price-field" style="left:196px;width:144px">Gold
    <svg style="position:absolute;right:5px;top:4px" width="10" height="10" viewBox="0 0 10 10"><rect width="10" height="10" rx="2" fill="#d9c9a6"/><path d="M2.5 4l2.5 3 2.5-3" fill="#5a4830"/></svg>
  </div>
  <span class="abs divider" style="left:354px"></span>
  <span class="abs price-label" style="left:369px">Last update
    <svg width="11" height="11" viewBox="0 0 11 11" style="vertical-align:-2px;margin-left:3px"><rect x="0.5" y="1.5" width="10" height="9" fill="#fff" stroke="#b33"/><rect x="0.5" y="1.5" width="10" height="3" fill="#c33"/></svg>
  </span>
  <div class="abs price-field" style="left:368px;width:143px">Thu May 30, 6:29 AM CDT</div>
  <span class="abs divider" style="left:524px"></span>
  <span class="abs price-label" style="left:539px">Bid</span>
  <span class="abs price-label" style="left:606px">Ask</span>
  <div class="abs price-field" style="left:538px;width:59px;padding-left:13px">1,400.36</div>
  <div class="abs price-field" style="left:605px;width:59px;padding-left:13px">1,400.98</div>
  <span class="abs divider" style="left:678px"></span>
  <span class="abs price-label" style="left:693px">Low</span>
  <span class="abs price-label" style="left:760px">High</span>
  <div class="abs price-field" style="left:692px;width:59px;padding-left:13px">1,389.12</div>
  <div class="abs price-field" style="left:759px;width:59px;padding-left:13px">1,410.86</div>
  <span class="abs divider" style="left:832px"></span>
  <span class="abs price-label" style="left:847px">Change</span>
  <div class="abs price-field" style="left:835px;width:79px;padding-left:23px">+6.99 (0.5%)</div>
  <span class="abs divider" style="left:931px"></span>
  <svg class="abs" style="left:944px;top:1148px" width="34" height="34" viewBox="0 0 34 34">
    <path d="M26 12A11 11 0 1 0 28 20" fill="none" stroke="#6e5a3c" stroke-width="4"/>
    <path d="M21 4l9 6-10 3z" fill="#6e5a3c"/>
  </svg>
</footer>

</body>
</html>
```